Email Signature

We would like to have an email Signature designed.
We have an idea, and a logo that we would like to be make more professional in design and look.

```html
<!DOCTYPE html>
<html lang="en">
<head>
<meta charset="utf-8">
<title>Email Signature – Brightlane Consulting</title>
<link rel="stylesheet" href="https://fonts.googleapis.com/css2?family=Montserrat:wght@600;700&family=Open+Sans:wght@400;600;700&display=swap">
<style>
  :root {
    --page-bg: #3a3a3a;
    --card-bg: #ffffff;
    --brand-blue: #1273bd;
    --brand-orange: #ef5a28;
    --text-grey: #555555;
    --text-white: #ffffff;
  }
  * { margin: 0; padding: 0; box-sizing: border-box; }
  html, body {
    width: 1040px;
    height: 1200px;
    overflow: hidden;
    background: var(--page-bg);
  }
  .signature {
    position: absolute;
    left: 40px;
    top: 462px;
    width: 960px;
    height: 275px;
    background: var(--card-bg);
    overflow: hidden;
  }
  .footer-band {
    position: absolute;
    left: 0;
    right: 0;
    bottom: 0;
    height: 58px;
    background: var(--brand-blue);
    border-top: 8px solid var(--brand-orange);
  }
  .contact {
    position: absolute;
    left: 80px;
    top: 83px;
  }
  .contact__name {
    font-family: "Montserrat", sans-serif;
    font-weight: 700;
    font-size: 17px;
    color: var(--brand-blue);
    letter-spacing: 0.2px;
    line-height: 1;
  }
  .contact__role {
    font-family: "Open Sans", sans-serif;
    font-size: 14.5px;
    color: var(--text-grey);
    margin-top: 4px;
    line-height: 1.2;
  }
  .contact__phone {
    font-family: "Open Sans", sans-serif;
    font-size: 14.5px;
    color: var(--text-grey);
    margin-top: 9px;
    line-height: 1.2;
  }
  .contact__label {
    color: var(--brand-orange);
    font-weight: 700;
  }
  .brand {
    position: absolute;
    right: 64px;
    top: 124px;
    display: flex;
    align-items: center;
    gap: 10px;
  }
  .brand__dot {
    width: 22px;
    height: 22px;
    border-radius: 50%;
    background: var(--brand-orange);
  }
  .brand__name {
    font-family: "Montserrat", sans-serif;
    font-weight: 700;
    font-size: 26px;
    color: var(--brand-blue);
    line-height: 1;
  }
  .website {
    position: absolute;
    left: 88px;
    bottom: 18px;
    font-family: "Open Sans", sans-serif;
    font-weight: 600;
    font-size: 14.5px;
    line-height: 1.2;
    color: var(--text-white);
  }
</style>
</head>
<body>
  <div class="signature">
    <div class="footer-band" aria-hidden="true"></div>

    <div class="contact">
      <p class="contact__name">TESS HARLAN</p>
      <p class="contact__role">Client Relations</p>
      <p class="contact__phone"><span class="contact__label">M:</span> +61412 555 018</p>
    </div>

    <div class="brand">
      <span class="brand__dot"></span>
      <span class="brand__name">Brightlane Consulting</span>
    </div>

    <p class="website">www.brightlane.com.au</p>
  </div>
</body>
</html>
```